Modern design for a watersports website

Building a brand new site for Kiteboarders/Kitesurfers .... this is the first of 8 sites we're rolling out.

We're as much looking for a partner to work with, and they will be chosen based on the winner of this site design.

It will need these menu pages:

1) How-To
2) Classifieds
3) Groups
4) News
5) Events

Width: 1150px

The home page, should feature:

1) A search box to enter a location
2) Under that, a series of boxes showing up to 5 previous locations chosen - these should be "buttons", directly under the location (i.e. no photo, just the location name)
3) Under that, a 5 x 3 grid of adverts, featuring a photo, a title & a price
4) Under that, top 5 headlines, each one featuring photo, headline & Summary
5) Under that, top 10 Group topics: Group, Title, Author, #Replies (no photo for these)
6) Under that, 5 x 3 grid of photos
7) Footer

Colours should be of the ocean:
Blues, greens, compatible with yellow. (i.e. not washed out blues like tessaloom), vibrant blues, but not too vivid as to overpower.

Avoid: Photos of any equipment, as they will date quickly.

Industry/Entity Type

Building

Number of Pages Required

1 page

Font styles to use
Sans Serif

Requirements
Must have
• Ocean colours; blues
Nice to have
• Modern design

```html
<!DOCTYPE html>
<html lang="en">
<head>
<meta charset="utf-8">
<title>TideRunner — Home</title>
<link rel="stylesheet" href="https://fonts.googleapis.com/css2?family=Oswald:wght@300;400;500;700&family=Open+Sans:wght@400;600;700&display=swap">
<style>
:root{
  --accent:#7ec242;
  --blue:#3d8ccc;
  --navy:#2a4f9d;
  --ink:#222;
  --muted:#555;
  --price:#e2542c;
  --paper:#fff;
  --soft:#f3f3f3;
  --dark:#141516;
  --darker:#0b0c0c;
  --line:#ddd;
}
*{box-sizing:border-box;margin:0;padding:0}
html,body{width:1200px;height:3905px;overflow:hidden;background:var(--paper)}
body{position:relative;font-family:"Open Sans",Arial,sans-serif;color:var(--ink)}
.abs{position:absolute}
.photo{display:block}
/* header */
.topline{top:0;left:0;width:1200px;height:5px;background:var(--accent)}
.site-header{top:5px;left:0;width:1200px;height:125px;background:var(--paper)}
.brand{left:99px;top:50px;font-family:"Oswald",sans-serif;font-weight:700;font-size:36px;color:var(--navy);letter-spacing:.5px;display:flex;align-items:center;gap:10px}
.brand i{display:block;width:14px;height:14px;border-radius:50%;background:var(--blue)}
.search{left:924px;top:26px;width:174px;height:32px;border:1px solid #e3e3e3;font-size:11px;color:#444;padding:8px 10px;display:flex;justify-content:space-between;align-items:center}
.nav{left:450px;top:81px;display:flex;font-size:11px;font-weight:600;text-transform:uppercase;color:#333}
.nav a{display:block;height:32px;line-height:32px;text-decoration:none;color:inherit}
.nav .home{background:var(--blue);color:#fff;width:73px;text-align:center}
/* hero */
.hero{top:130px;left:0;width:1200px;height:594px;overflow:hidden}
.hero .photo{position:absolute;inset:0;background:linear-gradient(180deg,#dde3e8 0%,#b9c7d3 38%,#3a79b3 62%,#174f86 100%);clip-path:polygon(0 0,100% 0,100% 72%,0 100%)}
.hero h1{position:absolute;left:99px;top:178px;font-family:"Oswald",sans-serif;font-weight:700;font-size:74px;color:var(--navy);letter-spacing:1px;line-height:1}
.hero p{position:absolute;left:99px;top:276px;width:520px;font-size:15px;font-weight:600;color:#1d2f55;line-height:1.5}
.arrow{position:absolute;top:236px;width:34px;height:34px;border-radius:50%;background:rgba(90,90,90,.55)}
/* sections */
.section-title{font-family:"Oswald",sans-serif;font-weight:400;font-size:28px;text-transform:uppercase;letter-spacing:.5px}
.loc-title{top:725px;right:102px;color:#222}
.row{display:flex;gap:18px}
.card{width:185px}
.card .photo{height:154px}
.card h3{font-size:11px;font-weight:600;text-transform:uppercase;margin-top:26px;color:#222}
.card p{font-size:11px;line-height:17px;color:#444;margin-top:8px}
.locations{top:791px;left:99px}
/* ads */
.ads{top:1104px;left:0;width:1200px;height:809px;background:linear-gradient(180deg,#2f7cc4 0%,#5fa8dc 35%,#9dd3ea 60%,#cfe7ef 100%)}
.ads .section-title{position:absolute;top:24px;width:100%;text-align:center;color:#fff}
.ad-grid{position:absolute;left:99px;top:93px;display:grid;grid-template-columns:repeat(5,185px);column-gap:18px;row-gap:29px}
.ad{background:#fff;height:203px;box-shadow:0 2px 4px rgba(0,0,0,.12)}
.ad .photo{height:135px}
.ad h3{font-family:"Oswald",sans-serif;font-weight:400;font-size:13px;text-transform:uppercase;padding:10px 16px 0;color:#333}
.ad span{display:block;font-family:"Oswald",sans-serif;font-size:13px;color:var(--price);padding:6px 16px}
/* headlines */
.headlines{top:1957px;left:99px}
.headline .label{height:34px;background:var(--blue);color:#fff;font-size:11px;font-weight:600;text-transform:uppercase;line-height:34px;padding-left:10px}
.headline .photo{height:156px}
.headline h3{margin-top:20px}
.headline .more{display:block;margin-top:12px;font-size:10px;font-weight:700;color:var(--navy);text-transform:uppercase}
/* group topics */
.groups{top:2322px;left:0;width:1200px;height:411px;background:var(--soft)}
.groups .section-title{position:absolute;top:26px;width:100%;text-align:center;color:#222}
.topic{position:absolute;top:94px;width:300px}
.topic .photo{height:164px}
.topic h3{font-size:11px;font-weight:600;text-transform:uppercase;margin-top:26px}
.topic .author{font-size:11px;color:#444;margin-top:10px;padding-bottom:10px;border-bottom:1px solid var(--line)}
.topic .meta{display:flex;justify-content:space-between;font-size:10px;margin-top:12px;color:#333}
.topic .meta b{font-weight:600;text-transform:uppercase}
/* photos */
.photos-title{top:2772px;width:1200px;text-align:center;color:#222}
.photo-grid{top:2842px;left:99px;display:grid;grid-template-columns:repeat(5,185px);column-gap:18px;row-gap:21px}
.photo-grid .photo{height:160px}
.hover{position:relative}
.hover .icons{position:absolute;top:70px;left:64px;display:flex;gap:12px}
.hover .icons i{width:22px;height:22px;border-radius:50%;background:rgba(0,0,0,.45)}
/* footer */
.site-footer{top:3394px;left:0;width:1200px;height:446px;background:var(--dark);clip-path:polygon(0 0,100% 44px,100% 100%,0 100%);color:#ddd}
.site-footer h4{position:absolute;top:119px;font-size:15px;font-weight:400;color:#fff}
.contact-item{position:absolute;left:99px;display:flex;gap:18px;font-size:11px}
.contact-item svg{flex:none}
.contact-item b{display:block;font-weight:600;text-transform:uppercase;font-size:12px;color:#fff;margin-bottom:6px}
.form{position:absolute;left:476px;top:119px;width:438px}
.field{height:31px;border:1px solid #444;font-size:11px;color:#888;padding:8px 10px;margin-bottom:16px}
.field.msg{height:82px}
.send{width:117px;height:32px;background:#000;color:#fff;font-size:10px;font-weight:600;text-transform:uppercase;line-height:32px;text-align:center;margin-top:4px}
.social{position:absolute;left:1002px;top:150px;list-style:none;font-size:11px}
.social li{display:flex;align-items:center;gap:12px;margin-bottom:14px}
.social li i{width:8px;height:8px;border-radius:50%;background:#ccc}
.bottom-bar{top:3840px;left:0;width:1200px;height:65px;background:var(--darker);color:#aaa;font-size:9px;text-transform:uppercase;text-align:center;line-height:65px}
</style>
</head>
<body>
<div class="abs topline"></div>
<header class="abs site-header">
  <div class="abs brand"><span>TideRunner</span><i></i></div>
  <div class="abs search"><span>Search</span><svg width="10" height="10" viewBox="0 0 10 10"><circle cx="4" cy="4" r="3" fill="none" stroke="#333" stroke-width="1.4"/><line x1="6.2" y1="6.2" x2="9.3" y2="9.3" stroke="#333" stroke-width="1.4"/></svg></div>
  <nav class="abs nav">
    <a class="home" href="#">Home</a>
    <a href="#" style="margin-left:55px">How-To</a>
    <a href="#" style="margin-left:66px">Classifieds</a>
    <a href="#" style="margin-left:44px">Groups</a>
    <a href="#" style="margin-left:50px">News</a>
    <a href="#" style="margin-left:58px">Events</a>
    <a href="#" style="margin-left:56px">Contact</a>
  </nav>
</header>

<section class="abs hero">
  <div class="photo" role="img" aria-label="Rider on a board skimming across a bright blue sea under a pale sky"></div>
  <svg class="abs" style="left:0;top:0" width="1200" height="594"><line x1="0" y1="594" x2="1200" y2="428" stroke="#3d8ccc" stroke-width="4"/></svg>
  <h1>TIDERUNNER</h1>
  <p>Sed ut perspiciatis unde omnis iste natus error sit voluptatem doloremque laudantium, totam rem aperiam,</p>
  <span class="arrow" style="left:30px"><svg width="34" height="34"><path d="M19 11l-6 6 6 6" fill="none" stroke="#fff" stroke-width="2"/></svg></span>
  <span class="arrow" style="right:30px"><svg width="34" height="34"><path d="M15 11l6 6-6 6" fill="none" stroke="#fff" stroke-width="2"/></svg></span>
</section>

<h2 class="abs section-title loc-title">5 Previous Locations Chosen</h2>
<div class="abs row locations">
  <article class="card"><div class="photo" role="img" aria-label="Rider riding a board on turquoise water" style="background:linear-gradient(#7fc2e8,#2b86c4)"></div><h3>Sed ut perspiciatis unde</h3><p>Lorem ipsum dolor sit amet, consectetur adipiscing elit, sed do eiusmod tempor</p></article>
  <article class="card"><div class="photo" role="img" aria-label="Couple walking on a sunny beach" style="background:linear-gradient(#d9eaf2,#c9a77a)"></div><h3>Sed ut perspiciatis unde</h3><p>Lorem ipsum dolor sit amet, consectetur adipiscing elit, sed do eiusmod tempor</p></article>
  <article class="card"><div class="photo" role="img" aria-label="Surfer walking the shore at sunset" style="background:linear-gradient(#e8c58a,#6d6a5e)"></div><h3>Sed ut perspiciatis unde</h3><p>Lorem ipsum dolor sit amet, consectetur adipiscing elit, sed do eiusmod tempor</p></article>
  <article class="card"><div class="photo" role="img" aria-label="Surfboard held up against the sea" style="background:linear-gradient(#e9f1f5,#4a9ccc)"></div><h3>Sed ut perspiciatis unde</h3><p>Lorem ipsum dolor sit amet, consectetur adipiscing elit, sed do eiusmod tempor</p></article>
  <article class="card"><div class="photo" role="img" aria-label="Rider gliding across open water" style="background:linear-gradient(#cfe1ee,#2f74b0)"></div><h3>Sed ut perspiciatis unde</h3><p>Lorem ipsum dolor sit amet, consectetur adipiscing elit, sed do eiusmod tempor</p></article>
</div>

<section class="abs ads" role="img" aria-label="Tropical sea and beach backdrop">
  <h2 class="section-title">Advertisement</h2>
  <div class="ad-grid">
    <div class="ad"><div class="photo" role="img" aria-label="Rider on waves" style="background:linear-gradient(#9fcbe8,#2a6ea8)"></div><h3>Sed ut perspiciatis unde</h3><span>$120.00</span></div>
    <div class="ad"><div class="photo" role="img" aria-label="Rider above clear water" style="background:linear-gradient(#8cc7ee,#1d8fc2)"></div><h3>Sed ut perspiciatis unde</h3><span>$120.00</span></div>
    <div class="ad"><div class="photo" role="img" aria-label="Boats in a lagoon" style="background:linear-gradient(#7cb9d9,#2c9a8e)"></div><h3>Sed ut perspiciatis unde</h3><span>$120.00</span></div>
    <div class="ad"><div class="photo" role="img" aria-label="Waterfront old town" style="background:linear-gradient(#a9c9e0,#6d7f7c)"></div><h3>Sed ut perspiciatis unde</h3><span>$120.00</span></div>
    <div class="ad"><div class="photo" role="img" aria-label="Resort pool with palms" style="background:linear-gradient(#4da8e2,#2fb8cf)"></div><h3>Sed ut perspiciatis unde</h3><span>$120.00</span></div>
    <div class="ad"><div class="photo" role="img" aria-label="Palm beach and sea" style="background:linear-gradient(#5eb2e6,#2aa7b5)"></div><h3>Sed ut perspiciatis unde</h3><span>$120.00</span></div>
    <div class="ad"><div class="photo" role="img" aria-label="Deck chairs on sand" style="background:linear-gradient(#87c4e4,#d7c190)"></div><h3>Sed ut perspiciatis unde</h3><span>$120.00</span></div>
    <div class="ad"><div class="photo" role="img" aria-label="White sand beach" style="background:linear-gradient(#a3d2ec,#e6dcc2)"></div><h3>Sed ut perspiciatis unde</h3><span>$120.00</span></div>
    <div class="ad"><div class="photo" role="img" aria-label="Limestone islands" style="background:linear-gradient(#7fbbe0,#3f8d6a)"></div><h3>Sed ut perspiciatis unde</h3><span>$120.00</span></div>
    <div class="ad"><div class="photo" role="img" aria-label="Green lakes and falls" style="background:linear-gradient(#6fae5f,#2d7d6d)"></div><h3>Sed ut perspiciatis unde</h3><span>$120.00</span></div>
    <div class="ad"><div class="photo" role="img" aria-label="Mountain lake village" style="background:linear-gradient(#9cc5e2,#4f6d55)"></div><h3>Sed ut perspiciatis unde</h3><span>$120.00</span></div>
    <div class="ad"><div class="photo" role="img" aria-label="Rock island in green bay" style="background:linear-gradient(#86c6e8,#3a9b8a)"></div><h3>Sed ut perspiciatis unde</h3><span>$120.00</span></div>
    <div class="ad"><div class="photo" role="img" aria-label="Domed city on a canal" style="background:linear-gradient(#9fcdec,#b79a70)"></div><h3>Sed ut perspiciatis unde</h3><span>$120.00</span></div>
    <div class="ad"><div class="photo" role="img" aria-label="Turquoise bay from above" style="background:linear-gradient(#3cb0b8,#1f7f8c)"></div><h3>Sed ut perspiciatis unde</h3><span>$120.00</span></div>
    <div class="ad"><div class="photo" role="img" aria-label="Stone bridge at dusk" style="background:linear-gradient(#6b9ccc,#b28a5a)"></div><h3>Sed ut perspiciatis unde</h3><span>$120.00</span></div>
  </div>
</section>

<div class="abs row headlines">
  <article class="card headline"><div class="label">Sed ut perspiciatis unde</div><div class="photo" role="img" aria-label="Rider jumping above the water" style="background:linear-gradient(#7aa8d6,#2a5d96)"></div><h3>Sed ut perspiciatis unde</h3><p>Lorem ipsum dolor sit amet, consectetur adipiscing elit, sed do eiusmod tempor</p><a class="more">Read more</a></article>
  <article class="card headline"><div class="label">Sed ut perspiciatis unde</div><div class="photo" role="img" aria-label="Spray behind a rider on dark water" style="background:linear-gradient(#22446e,#0f2640)"></div><h3>Sed ut perspiciatis unde</h3><p>Lorem ipsum dolor sit amet, consectetur adipiscing elit, sed do eiusmod tempor</p><a class="more">Read more</a></article>
  <article class="card headline"><div class="label">Sed ut perspiciatis unde</div><div class="photo" role="img" aria-label="Rider in mid-air against the sky" style="background:linear-gradient(#9ec4e6,#4d7fb4)"></div><h3>Sed ut perspiciatis unde</h3><p>Lorem ipsum dolor sit amet, consectetur adipiscing elit, sed do eiusmod tempor</p><a class="more">Read more</a></article>
  <article class="card headline"><div class="label">Sed ut perspiciatis unde</div><div class="photo" role="img" aria-label="Rider on calm blue sea" style="background:linear-gradient(#4f8fd0,#1e5ea4)"></div><h3>Sed ut perspiciatis unde</h3><p>Lorem ipsum dolor sit amet, consectetur adipiscing elit, sed do eiusmod tempor</p><a class="more">Read more</a></article>
  <article class="card headline"><div class="label">Sed ut perspiciatis unde</div><div class="photo" role="img" aria-label="Beach scene with palm trunk" style="background:linear-gradient(#6cb1e0,#b07a4a)"></div><h3>Sed ut perspiciatis unde</h3><p>Lorem ipsum dolor sit amet, consectetur adipiscing elit, sed do eiusmod tempor</p><a class="more">Read more</a></article>
</div>

<section class="abs groups">
  <h2 class="section-title">Group Topics</h2>
  <article class="topic" style="left:99px"><div class="photo" role="img" aria-label="Group gathered on a boat deck" style="background:linear-gradient(#b26a3f,#3d3a3a)"></div><h3>Sed ut perspiciatis unde</h3><div class="author">Author :&nbsp; Lena Hartwell, Omar Castell</div><div class="meta"><span>&#8630; Reply</span><b>Read more</b></div></article>
  <article class="topic" style="left:445px"><div class="photo" role="img" aria-label="Person resting on a lounger" style="background:linear-gradient(#d88a3c,#6a5a52)"></div><h3>Sed ut perspiciatis unde</h3><div class="author">Author :&nbsp; Lena Hartwell, Omar Castell</div><div class="meta"><span>&#8630; Reply</span><b>Read more</b></div></article>
  <article class="topic" style="left:794px"><div class="photo" role="img" aria-label="Rider silhouette in the air" style="background:linear-gradient(#a8a8a8,#6e6e6e)"></div><h3>Sed ut perspiciatis unde</h3><div class="author">Author :&nbsp; Lena Hartwell, Omar Castell</div><div class="meta"><span>&#8630; Reply</span><b>Read more</b></div></article>
</section>

<h2 class="abs section-title photos-title">Our Photos</h2>
<div class="abs photo-grid">
  <div class="photo" role="img" aria-label="Rider on turquoise water" style="background:linear-gradient(#7fc2e8,#2b86c4)"></div>
  <div class="photo" role="img" aria-label="Rider on deep blue water" style="background:linear-gradient(#5b9bd0,#1d5c98)"></div>
  <div class="photo hover" role="img" aria-label="Photo with zoom and link overlay" style="background:#2a4e5c"><span class="icons"><i></i><i></i></span></div>
  <div class="photo" role="img" aria-label="Rider on yellow board" style="background:linear-gradient(#8fbcb0,#c7a24a)"></div>
  <div class="photo" role="img" aria-label="Surfer on rocks by the sea" style="background:linear-gradient(#b8d4e6,#6d5a4c)"></div>
  <div class="photo" role="img" aria-label="Waterfall in green cliffs" style="background:linear-gradient(#6fae5f,#2d7d6d)"></div>
  <div class="photo" role="img" aria-label="Mountain lake village" style="background:linear-gradient(#9cc5e2,#4f6d55)"></div>
  <div class="photo" role="img" aria-label="Resort pool with palms" style="background:linear-gradient(#4da8e2,#2fb8cf)"></div>
  <div class="photo" role="img" aria-label="Domed city on a canal" style="background:linear-gradient(#9fcdec,#b79a70)"></div>
  <div class="photo" role="img" aria-label="Stone bridge at dusk" style="background:linear-gradient(#6b9ccc,#b28a5a)"></div>
  <div class="photo" role="img" aria-label="Surfer walking on sand" style="background:linear-gradient(#e3c896,#8b7a62)"></div>
  <div class="photo" role="img" aria-label="Surfer inside a wave" style="background:linear-gradient(#2e86b8,#0f4f7a)"></div>
  <div class="photo" role="img" aria-label="Rider jumping against blue sky" style="background:linear-gradient(#8fc1e8,#2f6aa8)"></div>
  <div class="photo" role="img" aria-label="Surfer on a breaking wave" style="background:linear-gradient(#3f86c0,#1b5586)"></div>
  <div class="photo" role="img" aria-label="Rider across open sea" style="background:linear-gradient(#cfe1ee,#2f74b0)"></div>
</div>

<footer class="abs site-footer">
  <h4 style="left:99px">Contact Us</h4>
  <div class="contact-item" style="top:166px"><svg width="14" height="18" viewBox="0 0 14 18"><path d="M7 1a6 6 0 0 0-6 6c0 4.5 6 10 6 10s6-5.5 6-10a6 6 0 0 0-6-6z" fill="#fff"/><circle cx="7" cy="7" r="2.2" fill="#141516"/></svg><div><b>Address</b>TideRunner 14/2 Harbour Lane Bayview<br>NSW 2104</div></div>
  <div class="contact-item" style="top:252px"><svg width="16" height="16" viewBox="0 0 16 16"><path d="M3 1l3 3-2 2c1 2 3 4 5 5l2-2 3 3-2 3C6 15 1 10 0 3z" fill="#fff"/></svg><div><b>Call us</b>+ 1 555 0142 7730</div></div>
  <div class="contact-item" style="top:328px"><svg width="16" height="12" viewBox="0 0 16 12"><rect x=".7" y=".7" width="14.6" height="10.6" fill="none" stroke="#fff" stroke-width="1.4"/><path d="M1 1l7 6 7-6" fill="none" stroke="#fff" stroke-width="1.4"/></svg><div><b>E - Mail</b>hello@tiderunner.example</div></div>
  <div class="form">
    <div class="field">Name</div>
    <div class="field">Email</div>
    <div class="field">Phone</div>
    <div class="field msg">Message</div>
    <div class="send">Send message</div>
  </div>
  <h4 style="left:1002px">Social Media</h4>
  <ul class="social">
    <li><i></i>tessaloom</li>
    <li><i></i>Chirpline</li>
    <li><i></i>Circlecast</li>
    <li><i></i>Reelhub</li>
  </ul>
</footer>
<div class="abs bottom-bar">Copyright 2015, tiderunner.example all rights reserved.</div>
</body>
</html>
```